Silverleaf upkeep services strata flyer

Looking for a flyer that will grab peoples attention also need to include some kind off promotional offer on there so they will hold onto the flyer . Would like approximateley 4 pictures of appartment blocks. Would like to include the following services. Building management Common area cleaning ,window cleaning, lawn mowing, gardening , pressure cleaning, carpet cleaning, bin cleaning. Handy man services.

Target Market(s)

appartment blocks/strata managers

Industry/Entity Type

Pressure Cleaning

Font styles to use
Serif

Colors
0355a3
ceddec
ec2027

Requirements
Must have
• company logo & colors contact details email: Info@silverleafupkeepservices.com.au
• Phone: 0438507721 website silverleafupkeepservices.com.au

```html
<!DOCTYPE html>
<html lang="en">
<head>
<meta charset="utf-8">
<title>Silverleaf upkeep services – strata flyer</title>
<link href="https://fonts.googleapis.com/css2?family=Source+Sans+3:wght@400;600;700;800&display=swap" rel="stylesheet">
<style>
  :root{
    --brand-blue:#0355a3;
    --deep-blue:#0a3f8c;
    --pale-blue:#ceddec;
    --alert-red:#ec2027;
    --ink:#1d2a44;
    --page:#eef0f3;
    --white:#ffffff;
  }
  *{box-sizing:border-box;margin:0;padding:0}
  html,body{width:1200px;height:873px;overflow:hidden;background:var(--page)}
  body{font-family:"Source Sans 3",Arial,sans-serif;color:var(--ink);position:relative}

  .flyer{position:absolute;left:390px;top:12px;width:420px;height:850px;background:var(--white);overflow:hidden;box-shadow:0 4px 18px rgba(0,0,0,.18)}
  .flyer-art{position:absolute;inset:0}

  .quote-ribbon{position:absolute;right:0;top:26px;height:30px;padding:0 18px 0 26px;background:var(--alert-red);color:var(--white);font-weight:800;font-size:15px;line-height:30px;letter-spacing:.3px;clip-path:polygon(0 0,100% 0,100% 100%,0 100%,12px 50%)}

  .brand{position:absolute;left:22px;top:70px;display:flex;align-items:center;gap:10px}
  .brand-dot{width:34px;height:34px;border-radius:50%;background:var(--brand-blue)}
  .brand-name{font-weight:800;font-size:20px;line-height:1.05;color:var(--brand-blue);width:150px}

  .services{position:absolute;left:28px;top:440px;right:16px}
  .services-title{font-weight:800;font-size:21px;line-height:21px;color:var(--brand-blue);text-transform:uppercase;white-space:nowrap}
  .service-cols{display:flex;gap:12px;margin-top:10px}
  .service-list{list-style:none}
  .service-list.primary{width:182px}
  .service-list.secondary{margin-top:-52px}
  .service-list li{font-size:15.5px;line-height:21px;color:var(--ink);display:flex;align-items:center;gap:7px;white-space:nowrap}
  .service-list li::before{content:"";width:10px;height:10px;border-radius:50%;flex:none;background:var(--alert-red)}

  .offer{position:absolute;left:0;right:0;top:664px;text-align:center}
  .offer-headline{color:var(--alert-red);font-size:15px;font-weight:600;line-height:18px}
  .offer-terms{font-size:11px;color:var(--ink);line-height:14px}

  .phone-box{position:absolute;left:40px;right:40px;top:704px;height:54px;border:1.5px dashed #9fb6d2;display:flex;align-items:center;justify-content:center;gap:16px;background:rgba(255,255,255,.35)}
  .phone-number{color:var(--alert-red);font-weight:800;font-size:30px;letter-spacing:.5px}
  .email{position:absolute;left:0;right:0;top:764px;text-align:center;color:var(--brand-blue);font-size:16px;font-weight:600}

  .footer-band{position:absolute;left:0;right:0;bottom:0;height:52px;background:var(--brand-blue);color:var(--white);display:flex;align-items:center;justify-content:center;font-size:20px;font-weight:600}
</style>
</head>
<body>
<main class="flyer">
  <svg class="flyer-art" width="420" height="850" viewBox="0 0 420 850">
    <defs>
      <linearGradient id="photoTone" x1="0" y1="0" x2="1" y2="1">
        <stop offset="0" stop-color="#9fb4c6"/>
        <stop offset=".5" stop-color="#c9d3d8"/>
        <stop offset="1" stop-color="#7f9b72"/>
      </linearGradient>
      <linearGradient id="lowerTint" x1="0" y1="0" x2="0" y2="1">
        <stop offset="0" stop-color="#dce7f3"/>
        <stop offset="1" stop-color="#c5d6ea"/>
      </linearGradient>
    </defs>
    <path role="img" aria-label="Photo collage of apartment blocks and a window cleaner at work"
          d="M0 230 C120 250 260 200 420 120 L420 420 L0 420 Z" fill="url(#photoTone)"/>
    <path d="M0 180 C120 230 260 190 420 90 L420 118 C260 210 120 260 0 222 Z" fill="#0a3f8c"/>
    <path d="M0 210 C140 250 280 200 420 110 L420 124 C280 214 140 264 0 228 Z" fill="#5e8fc9"/>
    <path d="M0 650 C140 636 280 604 420 572 L420 850 L0 850 Z" fill="url(#lowerTint)"/>
    <path d="M0 634 C140 620 280 588 420 556 L420 572 C280 604 140 636 0 650 Z" fill="#0355a3"/>
    <path d="M0 654 C140 640 280 608 420 576 L420 582 C280 614 140 646 0 660 Z" fill="#8fb2da"/>
  </svg>

  <div class="quote-ribbon">FREE QUOTES!</div>

  <div class="brand">
    <span class="brand-dot"></span>
    <span class="brand-name">Silverleaf upkeep services</span>
  </div>

  <section class="services">
    <h2 class="services-title">Our Cleaning<br>Services Include:</h2>
    <div class="service-cols">
      <ul class="service-list primary">
        <li>Building Management</li>
        <li>Common Area Cleaning</li>
        <li>Window Cleaning</li>
        <li>Lawn Mowing</li>
        <li>Gardening</li>
      </ul>
      <ul class="service-list secondary">
        <li>Pressure Cleaning</li>
        <li>Carpet Cleaning</li>
        <li>Bin Cleaning</li>
        <li>Handy Man Services</li>
        <li>Offices Pubs &amp; Clubs</li>
      </ul>
    </div>
  </section>

  <div class="offer">
    <p class="offer-headline">Present This Brochure For Your Free Initial Clean</p>
    <p class="offer-terms">conditions apply &amp; offer ends 31/07/2015</p>
  </div>

  <div class="phone-box">
    <svg class="phone-icon" width="26" height="40" viewBox="0 0 26 40" aria-hidden="true">
      <rect x="1" y="1" width="24" height="38" rx="5" fill="#ec2027"/>
      <rect x="4" y="6" width="18" height="24" rx="1" fill="#ffffff"/>
      <circle cx="13" cy="34" r="2" fill="#ffffff"/>
    </svg>
    <span class="phone-number">0438 507 721</span>
  </div>

  <p class="email">Info@silverleafupkeepservices.com.au</p>

  <footer class="footer-band">www.silverleafupkeepservices.com.au</footer>
</main>
</body>
</html>
```